House-share and Room Rental Website (With Focus on the Bedroom Landing Page)

Looking for website design for our House-share (executive accommodation) and room rental business.

Our company name is: Lodvenra could also be written as LodVenra or lodvenra. Either is fine .. just looking for a nice clean catchy logo to go with the design.

EXAMPLES
These are examples of other websites in this field that are doing well. this is a kind of baseline.
https://kelbrin.com.au/
https://www.tuvaplex.com/
https://www.nestorvi.com/
https://www.quillsa.net/
https://www.pendlebarrow.com.au/

Our business model is to rent rooms to people looking for high-quality accommodation. We fill the gap between those looking to rent rooms and those with rooms to rent. However, our model is slightly different from those already on the market as we looking to fill a massive gap in the market delivering upmarket rooms for rent.(Executive Accommodation) also in the back end will be coupled with a self management process in the back end.

We offer executive style accommodation that stands out above the rest. With special extras like fire safety.. and management processes that create happier homes. We are looking for a web design package that can help us grow and scale our business. We need a design that is captivating

Our MAIN focus is having a room landing page that stands out from the rest... The core of our business will rely on the promotion of the rooms in a share house... so the whole design relies on the BEDROOM landing page to drive results.

Target Market(s)

We have 2 markets we are aiming at ... the first market is people offering rooms to rent who want the highest rental return. The second market is people looking to rent safe, high-quality rooms, in houses that are well managed and looked after.

Industry/Entity Type

Share Economy

Logo Text

LodVenra

Number of Pages Required

5+ page

Font styles to use
Sans Serif

Colors
3276b5

Requirements
Must have
• A messaging system whereby we can create direct communication between those offering rooms and those looking for rooms.
• A call to action that says " Schedule an Inspection"
• Landing page for promoting rooms
• A home page for showing stock.
• Profile page for those selling rooms
• Profile page for those looking for rooms.
• A scheduling calendar for booking inspections
Nice to have
• Pages where new residents can lock in a room.. pay bond and rents.. and sign contracts
• Notifications
• SMS capabilities in the backend.
Should not have
• No script or handwriting fonts.

```html
<!DOCTYPE html>
<html lang="en">
<head>
<meta charset="utf-8">
<title>Lodvenra – Child Bedroom</title>
<link href="https://fonts.googleapis.com/css2?family=Roboto:wght@400;500;700&family=Montserrat:wght@600;700&family=Open+Sans:ital,wght@0,400;0,600;1,400&display=swap" rel="stylesheet">
<style>
:root{
  --blue:#1a7ef5;
  --chat-blue:#0f8cf0;
  --bubble-blue:#4fb5f5;
  --bubble-grey:#a9a9b4;
  --ink:#222;
  --muted:#8a8a8a;
  --panel:#f8f8fa;
  --band:#f1f1f3;
  --chat-body:#ebebeb;
  --orange:#f7941d;
  --green:#3bb54a;
  --tag:#3b3b3b;
  --cta:#0a9bd9;
  --pink:#f27f7f;
}
*{box-sizing:border-box;margin:0;padding:0}
html,body{width:1200px;height:1200px;overflow:hidden;background:#fff}
body{position:relative;font-family:'Roboto',sans-serif;color:var(--ink)}
.abs{position:absolute}

.stat{position:absolute;top:26px;display:flex;align-items:flex-start}
.stat svg{width:40px;height:50px;margin-right:27px;margin-top:2px}
.stat-num{font-family:'Roboto',sans-serif;font-weight:700;font-size:32px;color:var(--blue);line-height:36px}
.stat-label{font-weight:500;font-size:13px;margin-top:2px}

.section-title{position:absolute;left:0;width:1185px;text-align:center;font-family:'Roboto',sans-serif;font-weight:500;font-size:21px;letter-spacing:-.3px}
.section-sub{position:absolute;left:0;width:1185px;text-align:center;font-family:'Open Sans',sans-serif;font-size:12px;color:var(--muted)}

.card{position:absolute;top:241px;width:277px;height:296px;background:var(--panel);border-radius:0 0 6px 6px;overflow:hidden}
.card-photo{height:179px;position:relative}
.badge{position:absolute;top:11px;right:11px;height:18px;padding:0 8px;font-size:7.5px;font-weight:700;color:#fff;line-height:18px;border-radius:2px}
.badge.share{background:var(--orange)}
.badge.rent{background:var(--green)}
.price{position:absolute;left:12px;bottom:10px;height:28px;width:73px;background:var(--tag);color:#fff;font-weight:700;font-size:12px;line-height:28px;text-align:center;border-radius:3px}
.loc{position:absolute;top:201px;left:21px;font-size:8.5px;display:flex;align-items:center;gap:4px}
.card-title{position:absolute;top:224px;left:22px;font-family:'Montserrat',sans-serif;font-weight:600;font-size:15px}
.features{position:absolute;top:261px;left:0;right:0;height:35px;background:var(--band);display:flex;justify-content:center;align-items:center;gap:13px;font-size:8.5px;color:var(--muted)}
.features span{display:flex;align-items:center;gap:3px}

.dot{position:absolute;left:1104px;width:8px;border-radius:4px;background:#aaa}

.hero-photo{left:6px;top:562px;width:546px;height:458px;background:radial-gradient(ellipse at 55% 45%,#d9d6d2 0%,#ece9e6 40%,#fafafa 75%,#fff 100%)}
.pitch-title{left:618px;top:630px;font-family:'Montserrat',sans-serif;font-weight:700;font-size:24px;line-height:26px;width:380px}
.pitch-text{left:618px;top:694px;width:230px;font-family:'Open Sans',sans-serif;font-size:11.5px;line-height:20px;letter-spacing:.4px;color:#333;white-space:nowrap;overflow:hidden}
.field{position:absolute;left:618px;width:400px;height:37px;background:#ececec;border-radius:3px;display:flex;align-items:center;padding-left:14px;gap:10px;font-family:'Open Sans',sans-serif;font-style:italic;font-weight:600;font-size:8px;letter-spacing:.6px;color:#444}
.cta{left:619px;top:899px;width:188px;height:37px;background:var(--cta);border-radius:19px;color:#fff;font-weight:700;font-size:12px;text-align:center;line-height:37px}

.chat{left:837px;top:699px;width:347px;height:477px;background:#fff}
.chat-head{height:64px;background:var(--chat-blue);color:#fff;display:flex;align-items:center;padding-left:17px;font-family:'Roboto',sans-serif;font-weight:700;font-size:20px}
.chat-head .ctrl{margin-left:auto;display:flex;gap:10px;align-items:center;padding-right:23px}
.chat-body{position:absolute;top:64px;left:0;width:347px;height:311px;background:var(--chat-body)}
.bubble{position:absolute;font-family:'Roboto',sans-serif;font-size:14px;padding:0 13px;height:39px;line-height:39px;border-radius:2px}
.bubble.them{background:var(--bubble-grey);color:#222}
.bubble.me{background:var(--bubble-blue);color:#fff}
.scroll{position:absolute;right:13px;top:10px;width:6px;height:292px;background:#fff;border-radius:3px}
.scroll::before{content:"";position:absolute;inset:0 0 auto 0;height:192px;background:var(--chat-blue);border-radius:3px}
.chat-tools{position:absolute;top:387px;left:22px;display:flex;gap:12px}
.chat-input{position:absolute;top:415px;left:15px;width:318px;height:62px;border:1.5px solid #cfcfcf;border-radius:4px;font-family:'Open Sans',sans-serif;font-style:italic;font-size:12px;color:#888;padding:28px 0 0 13px}
.send{position:absolute;right:4px;top:5px;width:45px;height:52px;background:var(--blue);border-radius:3px;display:flex;align-items:center;justify-content:center}

.inspect{left:527px;top:1118px;width:146px;height:24px;background:var(--pink);color:#fff;font-weight:700;font-size:11px;letter-spacing:-.4px;text-align:center;line-height:24px}
.avatar{position:absolute;top:1191px;width:40px;height:40px;border-radius:50%;background:linear-gradient(#b89a7a,#8a6c55)}
</style>
</head>
<body>

<!-- stats -->
<div class="stat" style="left:192px">
  <svg viewBox="0 0 40 50" fill="none" stroke="#111" stroke-width="2.5"><circle cx="20" cy="18" r="16"/><circle cx="20" cy="18" r="10"/><path d="M15 20l5-5 5 5v4h-10z"/><path d="M10 30l-5 16 7-3 4 6 4-15M30 30l5 16-7-3-4 6-4-15"/></svg>
  <div><div class="stat-num">3587</div><div class="stat-label">Satisfied Clients</div></div>
</div>
<div class="stat" style="left:413px">
  <svg viewBox="0 0 40 50" fill="#111"><circle cx="20" cy="13" r="10" fill="none" stroke="#111" stroke-width="3"/><path d="M2 50v-10c0-8 7-13 18-13s18 5 18 13v10z"/></svg>
  <div><div class="stat-num">70</div><div class="stat-label">Employees</div></div>
</div>
<div class="stat" style="left:637px">
  <svg viewBox="0 0 46 50" style="width:46px;margin-right:20px" fill="#111"><path d="M4 22h32v8c0 10-7 16-16 16S4 40 4 30z"/><path d="M36 25h4a5 5 0 010 10h-5" fill="none" stroke="#111" stroke-width="3"/><path d="M18 18c-3-4 4-6 1-12M25 17c-2-3 3-5 1-9" fill="none" stroke="#111" stroke-width="2"/><rect x="2" y="46" width="36" height="3"/></svg>
  <div><div class="stat-num">685</div><div class="stat-label">Cups of Coffee</div></div>
</div>
<div class="stat" style="left:870px">
  <svg viewBox="0 0 40 50" fill="#111"><path d="M20 2L2 20h5v12h26V20h5z"/><path d="M2 38c8-6 18-6 26-2l10-2v6l-12 6H4z"/></svg>
  <div><div class="stat-num">2930</div><div class="stat-label">Total Rooms</div></div>
</div>

<!-- listings -->
<div class="section-title" style="top:139px">Child Bedroom</div>
<div class="section-sub" style="top:170px">This is our child Bedroom for your childrens</div>

<div class="card" style="left:162px">
  <div class="card-photo" role="img" aria-label="Pink child bedroom with canopy bed" style="background:linear-gradient(135deg,#f3b6d3,#e96aa8 55%,#f4d2e2)">
    <div class="badge share">FOR SHARE</div><div class="price">$625,000</div>
  </div>
  <div class="loc"><svg width="7" height="9" viewBox="0 0 7 9"><path d="M3.5 0a3.5 3.5 0 013.5 3.5C7 6 3.5 9 3.5 9S0 6 0 3.5A3.5 3.5 0 013.5 0z" fill="#222"/><circle cx="3.5" cy="3.5" r="1.3" fill="#fff"/></svg>GALTUR ( AUSTRIA )</div>
  <div class="card-title">Two Child Bedroom</div>
  <div class="features"><span>4 Beds</span><span>▬ 3 Bath</span><span>● 250m²</span><span>⌂ 2 Garages</span></div>
</div>

<div class="card" style="left:462px">
  <div class="card-photo" role="img" aria-label="Bright child bedroom with teal curtains" style="background:linear-gradient(135deg,#c9c6bd,#e9e7e2 45%,#6fc7c1 70%,#d8d4cc)">
    <div class="badge rent">FOR RENT</div><div class="price">$625,000</div>
  </div>
  <div class="loc"><svg width="7" height="9" viewBox="0 0 7 9"><path d="M3.5 0a3.5 3.5 0 013.5 3.5C7 6 3.5 9 3.5 9S0 6 0 3.5A3.5 3.5 0 013.5 0z" fill="#222"/><circle cx="3.5" cy="3.5" r="1.3" fill="#fff"/></svg>GALTUR ( AUSTRIA )</div>
  <div class="card-title">Two Child Bedroom</div>
  <div class="features"><span>▭ 4 Beds</span><span>▬ 3 Bath</span><span>● 250m²</span><span>⌂ 2 Garages</span></div>
</div>

<div class="card" style="left:762px">
  <div class="card-photo" role="img" aria-label="Child bed with bright pink printed bedding" style="background:linear-gradient(135deg,#f48fc0,#e0207f 50%,#f7a6cf)">
    <div class="badge rent">FOR RENT</div><div class="price">$625,000</div>
  </div>
  <div class="loc"><svg width="7" height="9" viewBox="0 0 7 9"><path d="M3.5 0a3.5 3.5 0 013.5 3.5C7 6 3.5 9 3.5 9S0 6 0 3.5A3.5 3.5 0 013.5 0z" fill="#222"/><circle cx="3.5" cy="3.5" r="1.3" fill="#fff"/></svg>GALTUR ( AUSTRIA )</div>
  <div class="card-title">Two Child Bedroom</div>
  <div class="features"><span>▭ 4 Beds</span><span>▬ 3 Bath</span><span>● 250m²</span><span>⌂ 2 Garages</span></div>
</div>

<div class="dot" style="top:340px;height:8px"></div>
<div class="dot" style="top:351px;height:8px"></div>
<div class="dot" style="top:364px;height:17px;background:var(--blue)"></div>

<!-- pitch -->
<div class="abs hero-photo" role="img" aria-label="Smiling agent in cardigan offering a handshake"></div>
<div class="abs pitch-title">This is Our Responsibility To Give Comfortable Rooms</div>
<div class="abs pitch-text">There are many variations of passages<br>ity have suffered alteration in some fo<br>words which don't look even slightly b</div>
<div class="field" style="top:779px"><svg width="8" height="8" viewBox="0 0 8 8" fill="#bbb"><circle cx="4" cy="2.3" r="2.2"/><path d="M0 8c0-3 8-3 8 0z"/></svg>Business</div>
<div class="field" style="top:824px"><svg width="9" height="7" viewBox="0 0 9 7" fill="#bbb"><rect width="9" height="7"/></svg>Email</div>
<div class="abs cta">Contact With us</div>

<!-- testimonials -->
<div class="section-title" style="top:1069px">Our Customar Says</div>
<div class="section-sub" style="top:1099px">Absolutely Stunning Design and Functionality</div>
<div class="abs inspect">SCHEDULE AN INSPECTION</div>
<div class="avatar" role="img" aria-label="Customer portrait" style="left:198px"></div>
<div class="avatar" role="img" aria-label="Customer portrait" style="left:498px"></div>
<div class="avatar" role="img" aria-label="Customer portrait" style="left:798px"></div>

<!-- chat -->
<div class="abs chat">
  <div class="chat-head">Lodvenra Could Live Chat
    <div class="ctrl">
      <svg width="22" height="18" viewBox="0 0 22 18"><rect x="0" y="15" width="22" height="2.5" fill="#fff"/></svg>
      <svg width="18" height="18" viewBox="0 0 18 18" stroke="#fff" stroke-width="2.2"><path d="M1 1l16 16M17 1L1 17"/></svg>
    </div>
  </div>
  <div class="chat-body">
    <div class="bubble them" style="left:20px;top:43px">Hi!</div>
    <svg class="abs" style="left:28px;top:34px" width="10" height="10"><path d="M0 0l10 10H0z" fill="var(--bubble-grey)"/></svg>
    <div class="bubble them" style="left:20px;top:96px">How may I help you?</div>
    <div class="bubble me" style="left:251px;top:148px">Hello!</div>
    <svg class="abs" style="left:295px;top:187px" width="10" height="10"><path d="M0 0h10L10 10z" fill="var(--bubble-blue)"/></svg>
    <div class="bubble me" style="left:120px;top:203px">I need help with the design.</div>
    <div class="scroll"></div>
  </div>
  <div class="chat-tools">
    <svg width="20" height="18" viewBox="0 0 20 18" fill="#555"><path d="M0 6h4l6-5v16l-6-5H0z"/><path d="M13 5c2 2 2 6 0 8M16 3c3 3 3 9 0 12" stroke="#555" stroke-width="1.6" fill="none"/></svg>
    <svg width="14" height="22" viewBox="0 0 14 22" fill="#555"><rect x="4" y="0" width="6" height="13" rx="3"/><path d="M1 9c0 8 12 8 12 0" stroke="#555" stroke-width="1.6" fill="none"/><rect x="6" y="15" width="2" height="6"/></svg>
  </div>
  <div class="chat-input">Type your message here...
    <div class="send"><svg width="28" height="18" viewBox="0 0 28 18" fill="#fff"><path d="M0 0l28 9L0 18l4-9z"/></svg></div>
  </div>
</div>

</body>
</html>
```